Banner Ad Design for Resume Builder Needed

For the ad copy and design of the ad, I leave that up to you. Keep in mind this is a do-it-yourself online resume builder. The site is simple to use and geared towards people who are unsure of how to write/create their own resume.

You can view the site (which isn't finished) and how it works at http://cvcrafter.demo.tplwerks.net/

I do not want the same color scheme or the logo used in the ad, just the most appealing ad for those looking to use a product like this

I need the ad in these sizes:

300x250, 728x90, 160x600, 468x60, 120x600, 300x100

```html
<!DOCTYPE html>
<html lang="en">
<head>
<meta charset="utf-8">
<title>Build Yourself Online Resume – Banner Set</title>
<link rel="stylesheet" href="https://fonts.googleapis.com/css2?family=Mulish:wght@300;800&family=Arimo:wght@400;700&display=swap">
<style>
  :root {
    --stage: #ece8e2;
    --panel: #46433c;
    --panel-deep: #3c3933;
    --accent: #f6b800;
    --headline: #f7c31c;
    --copy: #ffffff;
    --rule: #e9b712;
    --btn-top: #a9da62;
    --btn-bottom: #6eaa27;
    --btn-edge: #c9ec96;
    --btn-text: #f1f7e6;
    --photo-light: #eeebe4;
    --photo-mid: #cac6bc;
    --photo-dark: #8d887e;
  }
  * { box-sizing: border-box; margin: 0; padding: 0; }
  html, body { width: 958px; height: 1200px; overflow: hidden; }
  body { background: var(--stage); position: relative; font-family: "Arimo", Arial, sans-serif; }

  .banner {
    position: absolute;
    overflow: hidden;
    background: var(--panel);
    box-shadow: 0 2px 6px rgba(0,0,0,.28);
  }
  .photo {
    position: absolute; left: 0; top: 0;
    background: linear-gradient(140deg, var(--photo-light) 0%, var(--photo-mid) 55%, var(--photo-dark) 100%);
  }
  .shapes { position: absolute; inset: 0; width: 100%; height: 100%; }
  .shapes .panel-shape { fill: var(--panel); }
  .shapes .accent-shape { fill: var(--accent); }

  .headline { position: absolute; color: var(--headline); text-transform: uppercase; line-height: 1; }
  .headline span { display: block; white-space: nowrap; }
  .headline .light { font-family: "Mulish", "Century Gothic", sans-serif; font-weight: 300; letter-spacing: -.02em; }
  .headline .bold  { font-family: "Mulish", "Century Gothic", sans-serif; font-weight: 800; letter-spacing: -.02em; }

  .features { position: absolute; list-style: none; color: var(--copy); text-align: center; border-top: 1px solid var(--rule); }
  .features li { border-bottom: 1px solid var(--rule); line-height: 1.05; }

  .cta {
    position: absolute;
    display: flex; align-items: center; justify-content: center;
    border-radius: 999px;
    background: linear-gradient(180deg, var(--btn-top), var(--btn-bottom));
    border: 2px solid var(--btn-edge);
    box-shadow: 0 2px 3px rgba(0,0,0,.35);
    color: var(--btn-text);
    font-family: "Arimo", Arial, sans-serif; font-weight: 700;
    text-transform: uppercase; letter-spacing: .02em;
    text-shadow: 0 1px 1px rgba(0,0,0,.3);
    text-decoration: none;
  }

  /* 300 x 100 */
  .ad-300x100 { left: 169px; top: 394px; width: 382px; height: 127px; }
  .ad-300x100 .headline { right: 14px; top: 10px; text-align: right; font-size: 24px; }
  .ad-300x100 .cta { left: 228px; top: 87px; width: 96px; height: 26px; font-size: 11px; }

  /* 300 x 250 */
  .ad-300x250 { left: 169px; top: 554px; width: 382px; height: 318px; }
  .ad-300x250 .headline { right: 8px; top: 52px; text-align: right; font-size: 22px; }
  .ad-300x250 .features { left: 220px; top: 142px; width: 146px; }
  .ad-300x250 .features li { font-size: 14.5px; padding: 4px 0 3px; }
  .ad-300x250 .cta { left: 220px; top: 256px; width: 142px; height: 40px; font-size: 16px; }

  /* 160 x 600 */
  .ad-160x600 { left: 562px; top: 110px; width: 204px; height: 762px; }
  .ad-160x600 .headline { left: 0; right: 0; top: 346px; text-align: center; font-size: 33px; line-height: 1.1; }
  .ad-160x600 .headline .bold { font-size: 35px; }
  .ad-160x600 .features { left: 29px; top: 514px; width: 145px; }
  .ad-160x600 .features li { font-size: 14.5px; padding: 5px 0 5px; }
  .ad-160x600 .cta { left: 24px; top: 678px; width: 157px; height: 44px; font-size: 17px; }

  /* 120 x 600 */
  .ad-120x600 { left: 789px; top: 110px; width: 153px; height: 762px; }
  .ad-120x600 .headline { left: 0; right: 0; top: 369px; text-align: center; font-size: 26px; line-height: 1.05; }
  .ad-120x600 .headline .bold { font-size: 27px; }
  .ad-120x600 .features { left: 11px; top: 523px; width: 130px; }
  .ad-120x600 .features li { font-size: 12.5px; padding: 4px 0 4px; }
  .ad-120x600 .cta { left: 8px; top: 685px; width: 135px; height: 38px; font-size: 15px; }

  /* 468 x 60 */
  .ad-468x60 { left: 346px; top: 886px; width: 595px; height: 77px; }
  .ad-468x60 .headline { left: 170px; top: 6px; font-size: 29px; }
  .ad-468x60 .cta { left: 466px; top: 26px; width: 102px; height: 26px; font-size: 11px; }

  /* 728 x 90 */
  .ad-728x90 { left: 16px; top: 976px; width: 926px; height: 114px; }
  .ad-728x90 .headline { left: 232px; top: 20px; font-size: 35px; }
  .ad-728x90 .features { left: 534px; top: 14px; width: 146px; border-top: 0; }
  .ad-728x90 .features li { font-size: 14.5px; padding: 6px 0 4px; }
  .ad-728x90 .cta { left: 724px; top: 36px; width: 158px; height: 46px; font-size: 17px; }
</style>
</head>
<body>

<section class="banner ad-300x100" aria-label="300 by 100 banner">
  <div class="photo" style="width:160px;height:127px" role="img" aria-label="Photo of glasses and a pen resting on a printed resume"></div>
  <svg class="shapes" viewBox="0 0 382 127" aria-hidden="true">
    <polygon class="panel-shape" points="151,0 382,0 382,127 151,127"/>
    <polygon class="accent-shape" points="128,127 151,127 151,50"/>
  </svg>
  <h2 class="headline"><span class="light">Build Yourself</span><span class="bold">Online Resume</span></h2>
  <a class="cta" href="#">Learn More</a>
</section>

<section class="banner ad-300x250" aria-label="300 by 250 banner">
  <div class="photo" style="width:210px;height:318px" role="img" aria-label="Photo of glasses and a pen resting on a printed resume"></div>
  <svg class="shapes" viewBox="0 0 382 318" aria-hidden="true">
    <polygon class="panel-shape" points="206,0 382,0 382,318 206,318"/>
    <polygon class="accent-shape" points="168,318 206,318 206,95"/>
  </svg>
  <h2 class="headline"><span class="light">Build Yourself</span><span class="bold">Online Resume</span></h2>
  <ul class="features">
    <li>Create Professional<br>resume in minutes</li>
    <li>Dozen of template<br>to pick form</li>
  </ul>
  <a class="cta" href="#">Learn More</a>
</section>

<section class="banner ad-160x600" aria-label="160 by 600 banner">
  <div class="photo" style="width:204px;height:306px" role="img" aria-label="Photo of glasses and a pen resting on a printed resume"></div>
  <svg class="shapes" viewBox="0 0 204 762" aria-hidden="true">
    <polygon class="panel-shape" points="0,305 204,282 204,762 0,762"/>
    <polygon class="accent-shape" points="0,252 150,288 0,305"/>
  </svg>
  <h2 class="headline"><span class="light">Build</span><span class="light">Yourself</span><span class="bold">Online</span><span class="bold">Resume</span></h2>
  <ul class="features">
    <li>Create Professional<br>resume in minutes</li>
    <li>Dozen of template<br>to pick form</li>
  </ul>
  <a class="cta" href="#">Learn More</a>
</section>

<section class="banner ad-120x600" aria-label="120 by 600 banner">
  <div class="photo" style="width:153px;height:306px" role="img" aria-label="Photo of glasses and a pen resting on a printed resume"></div>
  <svg class="shapes" viewBox="0 0 153 762" aria-hidden="true">
    <polygon class="panel-shape" points="0,305 153,282 153,762 0,762"/>
    <polygon class="accent-shape" points="0,252 113,288 0,305"/>
  </svg>
  <h2 class="headline"><span class="light">Build</span><span class="light">Yourself</span><span class="bold">Online</span><span class="bold">Resume</span></h2>
  <ul class="features">
    <li>Create Professional<br>resume in minutes</li>
    <li>Dozen of template<br>to pick form</li>
  </ul>
  <a class="cta" href="#">Learn More</a>
</section>

<section class="banner ad-468x60" aria-label="468 by 60 banner">
  <div class="photo" style="width:145px;height:77px" role="img" aria-label="Photo of glasses and a pen resting on a printed resume"></div>
  <svg class="shapes" viewBox="0 0 595 77" aria-hidden="true">
    <polygon class="panel-shape" points="142,0 595,0 595,77 142,77"/>
    <polygon class="accent-shape" points="118,77 142,77 142,20"/>
  </svg>
  <h2 class="headline"><span class="light">Build Yourself</span><span class="bold">Online Resume</span></h2>
  <a class="cta" href="#">Learn More</a>
</section>

<section class="banner ad-728x90" aria-label="728 by 90 banner">
  <div class="photo" style="width:222px;height:114px" role="img" aria-label="Photo of glasses and a pen resting on a printed resume"></div>
  <svg class="shapes" viewBox="0 0 926 114" aria-hidden="true">
    <polygon class="panel-shape" points="218,0 926,0 926,114 218,114"/>
    <polygon class="accent-shape" points="190,114 218,114 218,30"/>
  </svg>
  <h2 class="headline"><span class="light">Build Yourself</span><span class="bold">Online Resume</span></h2>
  <ul class="features">
    <li>Create Professional<br>resume in minutes</li>
    <li>Dozen of template<br>to pick form</li>
  </ul>
  <a class="cta" href="#">Learn More</a>
</section>

</body>
</html>
```